Design mobile friendly real estate and property management company landing page

Design a clean, crisp modern looking landing page that is mobile-friendly (must resize, preferably using bootstrap framework). Landing page will consist of heading with login area, company info, body consists of company description and services, a list of available rental properties with photos, and a footer with additional links and info. Working on updating with text for text areas marked A, B, and C on the layout pdf, but in meantime, lorem ipsum is fine. I can connect events to most buttons, etc. Just need the bootstrap and html functionality set up. Previous company website (which should not be relied upon) is www.kbtq.net This is somewhat of a template for a start, but looking for a more professional and modern design for the new website. But this gives an idea of the content and what needs to be displayed, and how.

Target Market(s)

Clients looking for a property management company that is efficient and well-organized.

Industry/Entity Type

Property Management

Coding

Coded - Design and coding required

Number of Pages Required

1 page

Font styles to use
Sans Serif

Colors
0355a3

Requirements
Must have
• Resize for the screen using bootstrap.
• Navigation that collapses for mobile devices
• Large text boxes and good solid spacing around all elements.
Nice to have
• for property images it would be nice if they can be swiped on touch enabled devices (to the next or previous image). And have navigation that can be clicked to next or previous images.
• Would be nice if a captcha verification was included on contact form.
Should not have
• Fancy or eccentric art

```html
<!DOCTYPE html>
<html lang="en">
<head>
<meta charset="utf-8">
<title>Harborline Property Group</title>
<link href="https://fonts.googleapis.com/css2?family=Open+Sans:wght@400;600;700&family=Roboto:wght@400;500;700&display=swap" rel="stylesheet">
<style>
:root{
  --primary:#0355a3;
  --navy:#111a2e;
  --nav-bg:#232425;
  --text:#333;
  --muted:#555;
  --line:#d6d6d6;
  --band:#f3f3f3;
  --listing-bg:#e4e4e4;
  --footer:#2a2a2a;
  --footer-bottom:#1c1c1c;
  --footer-text:#c9c9c9;
}
*{box-sizing:border-box;margin:0;padding:0}
html,body{width:1200px;height:2459px;overflow:hidden}
body{font-family:"Open Sans",sans-serif;color:var(--text);background:#fff;position:relative}
.abs{position:absolute}
svg{display:block}

/* top bar */
.topbar{left:0;top:0;width:1200px;height:31px;background:var(--navy);color:#fff;font-size:12px}
.topbar .item{position:absolute;top:8px;display:flex;align-items:center;gap:8px}
.header{left:0;top:31px;width:1200px;height:87px;background:#fff}
.brand{position:absolute;left:69px;top:12px;width:280px;text-align:center;color:var(--navy)}
.brand .name{font-family:"Roboto",sans-serif;font-weight:500;font-size:30px;letter-spacing:1px;line-height:34px}
.brand .sub{font-family:"Roboto",sans-serif;font-weight:500;font-size:15px;letter-spacing:5px;margin-top:2px}
.login{position:absolute;left:1021px;top:26px;width:112px;height:35px;background:#8a8a8a;color:#fff;font-size:13px;display:flex;align-items:center;justify-content:center;letter-spacing:.5px}

.nav{left:0;top:118px;width:1200px;height:46px;background:var(--nav-bg)}
.nav a{position:absolute;top:0;height:46px;line-height:46px;color:#fff;font-size:12px;font-weight:600;text-decoration:none;transform:translateX(-50%);white-space:nowrap}
.nav .sep{position:absolute;top:8px;width:1px;height:30px;background:#3d3e40}

/* hero */
.hero{left:0;top:164px;width:1200px;height:543px;background:linear-gradient(180deg,#7fa7a0 0%,#a9c3b2 35%,#c7d6bd 55%,#4c5a5e 72%,#1c2026 100%)}
.hero-copy{left:67px;top:110px;width:540px;color:var(--navy)}
.hero-copy .welcome{font-family:"Roboto",sans-serif;font-size:26px}
.hero-copy h1{font-family:"Roboto",sans-serif;font-weight:700;font-size:37px;letter-spacing:.3px;margin-top:2px}
.hero-copy p{font-size:13.5px;line-height:23px;margin-top:20px;color:#1e2636}
.btn{background:var(--primary);color:#fff;font-size:12px;font-weight:700;display:flex;align-items:center;justify-content:center;gap:14px;letter-spacing:.3px}
.readmore{left:66px;top:356px;width:152px;height:49px}
.slide-arrow{top:224px;width:36px;height:64px;background:rgba(60,60,60,.6);display:flex;align-items:center;justify-content:center}

.contact{left:797px;top:42px;width:383px;height:455px;background:rgba(18,26,44,.88);padding:0 29px}
.contact h2{font-family:"Open Sans",sans-serif;font-weight:600;color:#fff;font-size:22px;text-align:center;margin:22px 0 20px}
.field{background:#fff;height:43px;margin-bottom:13px;font-size:12px;color:#777;padding:0 14px;display:flex;align-items:center;justify-content:space-between}
.field.area{height:61px;align-items:flex-start;padding-top:14px}
.send{height:40px;margin-top:20px;font-size:13px;font-weight:600}

/* badges */
.badges{left:0;top:707px;width:1200px;height:94px;background:var(--band)}
.badge{position:absolute}

/* services */
.services{left:0;top:801px;width:1200px;height:564px;background:#fff}
.divider{left:600px;top:801px;width:1px;height:564px;background:#e2e2e2}
.svc{width:467px}
.svc h2{display:flex;align-items:center;justify-content:center;gap:16px;font-weight:400;font-size:27px;color:#1a1a1a}
.svc p{font-size:13.5px;line-height:24px;margin-top:34px;color:var(--muted)}
.svc ul{list-style:none;margin-top:40px}
.svc li{display:flex;align-items:center;gap:18px;height:46px;border-bottom:2px solid var(--line);font-size:15px;font-weight:600;color:#222}
.svc li:first-child{height:54px}
.svc li .arr{margin-left:auto}
.viewmore{width:122px;height:40px;margin-top:38px;font-size:12px;font-weight:600}

/* listings */
.listings{left:0;top:1365px;width:1200px;height:769px;background:var(--listing-bg)}
.listings h2{position:absolute;left:67px;top:73px;font-family:"Open Sans",sans-serif;font-weight:600;font-size:27px;color:#1a1a1a}
.card{left:66px;width:1068px;height:257px;background:#fff}
.card .kind{position:absolute;left:21px;top:14px;font-size:23px;color:var(--primary)}
.card .photo{position:absolute;left:19px;top:65px;width:253px;height:172px}
.card .photo .nav-l,.card .photo .nav-r{position:absolute;top:64px;width:22px;height:44px;background:rgba(0,0,0,.6);display:flex;align-items:center;justify-content:center}
.card .photo .nav-l{left:0;border-radius:0 22px 22px 0}
.card .photo .nav-r{right:0;border-radius:22px 0 0 22px}
.card .title{position:absolute;left:301px;top:20px;display:flex;align-items:center;gap:13px;font-size:15.5px;font-weight:600;color:#1a1a1a}
.card .facts{position:absolute;left:299px;top:65px;width:487px;height:172px;background:#eeefef;font-size:12px}
.facts .row{position:absolute;left:24px;width:440px;display:flex}
.facts .k{width:82px;font-weight:600;color:#222;font-size:13px}
.facts .v{width:160px;color:#555}
.facts .k2{width:112px;font-weight:600;color:#222;font-size:13px}
.card .side{position:absolute;left:816px;top:20px;width:240px}
.side h3{font-size:18px;font-weight:600;color:#1a1a1a}
.side .feat{display:flex;align-items:center;gap:12px;font-size:13px;font-weight:600;margin-top:14px}
.side .feat + .feat{margin-top:10px}
.side p{font-size:13px;line-height:24px;color:#555;margin-top:16px}

/* footer */
.footer{left:0;top:2134px;width:1200px;height:272px;background:var(--footer);color:var(--footer-text)}
.fcol{position:absolute;top:49px}
.fcol h4{font-weight:400;font-size:15px;color:#e5e5e5;padding-bottom:12px;border-bottom:1px solid #3c3c3c}
.fcol ul{list-style:none;margin-top:10px}
.fcol li{font-size:12px;line-height:26.5px}
.fcol li::before{content:"›";margin-right:6px}
.fsep{position:absolute;top:70px;width:1px;height:160px;background:#3a3a3a}
.contact-line{display:flex;gap:14px;font-size:12px;line-height:22px;margin-top:12px}
.flogo{position:absolute;left:955px;top:82px;width:205px;text-align:center;color:#fff}
.flogo .name{font-family:"Roboto",sans-serif;font-size:21px;letter-spacing:1px}
.flogo .sub{font-family:"Roboto",sans-serif;font-size:11px;letter-spacing:4px;margin-top:2px}
.copyright{left:0;top:2406px;width:1200px;height:53px;background:var(--footer-bottom);color:#bbb;font-size:12px;display:flex;align-items:center;justify-content:center}
</style>
</head>
<body>

<div class="abs topbar">
  <div class="item" style="left:787px">
    <svg width="13" height="10" viewBox="0 0 13 10"><rect width="13" height="10" fill="#fff"/><path d="M0 0l6.5 5L13 0" stroke="#111a2e" fill="none"/></svg>
    info@harborlinepg.com
  </div>
  <div class="item" style="left:1038px">
    <svg width="11" height="11" viewBox="0 0 24 24"><path fill="#fff" d="M6.6 10.8a15 15 0 006.6 6.6l2.2-2.2c.3-.3.7-.4 1-.2 1.1.4 2.3.6 3.6.6.6 0 1 .4 1 1V20c0 .6-.4 1-1 1A17 17 0 013 4c0-.6.4-1 1-1h3.5c.6 0 1 .4 1 1 0 1.3.2 2.5.6 3.6.1.3 0 .7-.2 1z"/></svg>
    555-014-2290
  </div>
</div>

<header class="abs header">
  <div class="brand"><div class="name">HARBORLINE</div><div class="sub">PROPERTY GROUP</div></div>
  <div class="login">LOG IN</div>
</header>

<nav class="abs nav">
  <a style="left:139px">HOME</a><span class="sep" style="left:211px"></span>
  <a style="left:295px">FOR RENT</a><span class="sep" style="left:379px"></span>
  <a style="left:461px">FOR SALE</a><span class="sep" style="left:545px"></span>
  <a style="left:674px">PROPERTY MANGEMENT</a><span class="sep" style="left:806px"></span>
  <a style="left:897px">REAL ESTATE</a><span class="sep" style="left:990px"></span>
  <a style="left:1065px">ABOUT</a>
</nav>

<section class="abs hero" role="img" aria-label="Photo of a waterfront city skyline at dusk framed by palm trees">
  <div class="abs hero-copy">
    <div class="welcome">Welcome to</div>
    <h1>HARBORLINE PROPERTY GROUP</h1>
    <p>Lorem ipsum dolor sit amet, consectetuer adipiscing elit, sed diam nonummy nibh euismod tincidunt ut laoreet dolore magna aliquam erat volutpat. Ut wisi enim ad minim veniam, quis nostrud exerci tation ullamcorper suscipit lobortis nisl aliquip ex ea commodo consequat.</p>
  </div>
  <div class="abs btn readmore">READ MORE
    <svg width="26" height="8" viewBox="0 0 26 8"><path d="M0 4h24M20 1l4 3-4 3" stroke="#fff" stroke-width="1.5" fill="none"/></svg>
  </div>
  <div class="abs slide-arrow" style="left:0;border-radius:0 32px 32px 0"><svg width="10" height="16" viewBox="0 0 10 16"><path d="M8 1L2 8l6 7" stroke="#fff" stroke-width="2" fill="none"/></svg></div>
  <div class="abs slide-arrow" style="left:1164px;border-radius:32px 0 0 32px"><svg width="10" height="16" viewBox="0 0 10 16"><path d="M2 1l6 7-6 7" stroke="#fff" stroke-width="2" fill="none"/></svg></div>

  <form class="abs contact">
    <h2>CONTACT US</h2>
    <div class="field">Name:</div>
    <div class="field">Phone:</div>
    <div class="field">Email:</div>
    <div class="field">Subject Property:
      <svg width="10" height="6" viewBox="0 0 10 6"><path d="M1 1l4 4 4-4" stroke="#999" fill="none"/></svg></div>
    <div class="field area">Comments:</div>
    <div class="btn send">
      <svg width="24" height="20" viewBox="0 0 24 20"><path fill="#fff" d="M0 9L24 0 19 20 11 14 9 20 8 12 20 3 6 11z"/></svg>
      SEND
    </div>
  </form>
</section>

<section class="abs badges" aria-label="Accreditations">
  <div class="badge" style="left:423px;top:22px;width:128px;height:48px;background:#1d5673;border-radius:3px"></div>
  <div class="badge" style="left:598px;top:22px;width:52px;height:50px;background:#8c8c8c"></div>
  <div class="badge" style="left:696px;top:22px;width:82px;height:50px;background:#eef3f8;border:1px solid #b8c8d8"></div>
</section>

<section class="abs services"></section>
<div class="abs divider"></div>

<div class="abs svc" style="left:67px;top:875px">
  <h2>
    <svg width="42" height="34" viewBox="0 0 42 34"><path d="M2 2v30h38" stroke="#0355a3" stroke-width="3" fill="none"/><rect x="8" y="18" width="5" height="12" fill="#0355a3"/><rect x="16" y="12" width="5" height="18" fill="#0355a3"/><rect x="24" y="16" width="5" height="14" fill="#0355a3"/><rect x="32" y="8" width="5" height="22" fill="#0355a3"/></svg>
    Property Management
  </h2>
  <p>Lorem ipsum dolor sit amet, consectetuer adipiscing elit, sed diam nonummy nibh euismod tincidunt ut laoreet dolore magna aliquam erat volutpat. Ut wisi enim ad minim veniam, quis nostrud exerci tation ullamcorper suscipit lobortis nisl aliquip ex ea commodo consequat.</p>
  <ul>
    <li><svg width="16" height="15" viewBox="0 0 16 15"><path fill="#111a2e" d="M8 0l8 7h-2v8H2V7H0z"/></svg>Properties Management<svg class="arr" width="26" height="12" viewBox="0 0 26 12"><path d="M0 6h24M19 1l5 5-5 5" stroke="#444" stroke-width="1.5" fill="none"/></svg></li>
    <li><svg width="16" height="15" viewBox="0 0 16 15"><path fill="#111a2e" d="M8 0l8 7h-2v8H2V7H0z"/></svg>Property Analysis<svg class="arr" width="26" height="12" viewBox="0 0 26 12"><path d="M0 6h24M19 1l5 5-5 5" stroke="#444" stroke-width="1.5" fill="none"/></svg></li>
    <li><svg width="16" height="15" viewBox="0 0 16 15"><path fill="#111a2e" d="M8 0l8 7h-2v8H2V7H0z"/></svg>Marketing and Leasing<svg class="arr" width="26" height="12" viewBox="0 0 26 12"><path d="M0 6h24M19 1l5 5-5 5" stroke="#444" stroke-width="1.5" fill="none"/></svg></li>
  </ul>
  <div class="btn viewmore" style="margin-left:3px">VIEW MORE</div>
</div>

<div class="abs svc" style="left:667px;top:875px">
  <h2>
    <svg width="46" height="38" viewBox="0 0 46 38"><path fill="#0355a3" d="M23 2L2 20h6v16h11V26h8v10h11V20h6z"/></svg>
    Real Estate
  </h2>
  <p>Lorem ipsum dolor sit amet, consectetuer adipiscing elit, sed diam nonummy nibh euismod tincidunt ut laoreet dolore magna aliquam erat volutpat. Ut wisi enim ad minim veniam, quis nostrud exerci tation ullamcorper suscipit lobortis nisl aliquip ex ea commodo consequat.</p>
  <ul>
    <li><svg width="16" height="15" viewBox="0 0 16 15"><path fill="#111a2e" d="M8 0l8 7h-2v8H2V7H0z"/></svg>Real Estate Consulting<svg class="arr" width="26" height="12" viewBox="0 0 26 12"><path d="M0 6h24M19 1l5 5-5 5" stroke="#444" stroke-width="1.5" fill="none"/></svg></li>
    <li><svg width="16" height="15" viewBox="0 0 16 15"><path fill="#111a2e" d="M8 0l8 7h-2v8H2V7H0z"/></svg>Sales<svg class="arr" width="26" height="12" viewBox="0 0 26 12"><path d="M0 6h24M19 1l5 5-5 5" stroke="#444" stroke-width="1.5" fill="none"/></svg></li>
    <li><svg width="16" height="15" viewBox="0 0 16 15"><path fill="#111a2e" d="M8 0l8 7h-2v8H2V7H0z"/></svg>Estate Management<svg class="arr" width="26" height="12" viewBox="0 0 26 12"><path d="M0 6h24M19 1l5 5-5 5" stroke="#444" stroke-width="1.5" fill="none"/></svg></li>
  </ul>
  <div class="btn viewmore" style="margin-left:3px">VIEW MORE</div>
</div>

<section class="abs listings">
  <h2>FEATURED LISTINGS</h2>
</section>

<article class="abs card" style="top:1505px">
  <div class="kind">For Rent</div>
  <div class="photo" role="img" aria-label="Photo of a bright modern living room with large windows" style="background:linear-gradient(135deg,#d9dcdc 0%,#f2f2f0 45%,#9aa39b 75%,#3a3d3d 100%)">
    <div class="nav-l"><svg width="7" height="12" viewBox="0 0 7 12"><path d="M6 1L1 6l5 5" stroke="#fff" stroke-width="1.6" fill="none"/></svg></div>
    <div class="nav-r"><svg width="7" height="12" viewBox="0 0 7 12"><path d="M1 1l5 5-5 5" stroke="#fff" stroke-width="1.6" fill="none"/></svg></div>
  </div>
  <div class="title"><svg width="16" height="20" viewBox="0 0 16 20"><path d="M8 19s7-7 7-11.5A7 7 0 001 7.5C1 12 8 19 8 19z" stroke="#222" stroke-width="2" fill="none"/><circle cx="8" cy="7.5" r="2.5" fill="#222"/></svg>Lorem ipsum dolor sit amet, consectetuer adipiscing elit</div>
  <div class="facts">
    <div class="row" style="top:20px"><span class="k">Rent :</span><span class="v">$1,600.00</span><span class="k2">Community :</span><span class="v">North Park</span></div>
    <div class="row" style="top:57px"><span class="k">Available :</span><span class="v">6/1/2016</span><span class="k2">Parking:</span><span class="v">2 assigned spaces</span></div>
    <div class="row" style="top:94px"><span class="k">Sqft :</span><span class="v">675</span><span class="k2">Pets :</span><span class="v">Inquire</span></div>
    <div class="row" style="top:130px"><span class="k">Lease :</span><span class="v">12 Months</span><span class="k2">Laundry :</span><span class="v">On-Site</span></div>
  </div>
  <div class="side">
    <h3>Suscipit Lobortis</h3>
    <div class="feat"><svg width="30" height="20" viewBox="0 0 30 20"><path d="M2 2v17M2 14h26v5M2 10h26v4" stroke="#0355a3" stroke-width="2.5" fill="none"/><rect x="5" y="5" width="7" height="5" fill="#0355a3"/></svg>2 Bedroom</div>
    <div class="feat"><svg width="30" height="20" viewBox="0 0 30 20"><path d="M2 8h26v3c0 5-4 7-8 7H10c-4 0-8-2-8-7z" fill="#0355a3"/><path d="M6 8V3h5" stroke="#0355a3" stroke-width="2" fill="none"/></svg>1 Bath Condo</div>
    <p>Lorem ipsum dolor sit amet, conse adipiscing elit, sed diam nonu nibh euismod tincidunt ut laoreet dolore magna aliquam er volutpat.</p>
  </div>
</article>

<article class="abs card" style="top:1801px">
  <div class="kind">For Sale</div>
  <div class="photo" role="img" aria-label="Photo of a modern house with a pool at dusk" style="background:linear-gradient(180deg,#5d8fc9 0%,#9ec0e0 40%,#e8e2d0 58%,#4d6a4a 80%,#3b9ec9 100%)">
    <div class="nav-l"><svg width="7" height="12" viewBox="0 0 7 12"><path d="M6 1L1 6l5 5" stroke="#fff" stroke-width="1.6" fill="none"/></svg></div>
    <div class="nav-r"><svg width="7" height="12" viewBox="0 0 7 12"><path d="M1 1l5 5-5 5" stroke="#fff" stroke-width="1.6" fill="none"/></svg></div>
  </div>
  <div class="title"><svg width="16" height="20" viewBox="0 0 16 20"><path d="M8 19s7-7 7-11.5A7 7 0 001 7.5C1 12 8 19 8 19z" stroke="#222" stroke-width="2" fill="none"/><circle cx="8" cy="7.5" r="2.5" fill="#222"/></svg>Lorem ipsum dolor sit amet, consectetuer adipiscing elit</div>
  <div class="facts">
    <div class="row" style="top:20px"><span class="k">Rent :</span><span class="v">$1,600.00</span><span class="k2">Community :</span><span class="v">North Park</span></div>
    <div class="row" style="top:57px"><span class="k">Available :</span><span class="v">6/1/2016</span><span class="k2">Parking:</span><span class="v">2 assigned spaces</span></div>
    <div class="row" style="top:94px"><span class="k">Sqft :</span><span class="v">675</span><span class="k2">Pets :</span><span class="v">Inquire</span></div>
    <div class="row" style="top:130px"><span class="k">Lease :</span><span class="v">12 Months</span><span class="k2">Laundry :</span><span class="v">On-Site</span></div>
  </div>
  <div class="side">
    <h3>Suscipit Lobortis</h3>
    <div class="feat"><svg width="30" height="20" viewBox="0 0 30 20"><path d="M2 2v17M2 14h26v5M2 10h26v4" stroke="#0355a3" stroke-width="2.5" fill="none"/><rect x="5" y="5" width="7" height="5" fill="#0355a3"/></svg>2 Bedroom</div>
    <div class="feat"><svg width="30" height="20" viewBox="0 0 30 20"><path d="M2 8h26v3c0 5-4 7-8 7H10c-4 0-8-2-8-7z" fill="#0355a3"/><path d="M6 8V3h5" stroke="#0355a3" stroke-width="2" fill="none"/></svg>1 Bath Condo</div>
    <p>Lorem ipsum dolor sit amet, conse adipiscing elit, sed diam nonu nibh euismod tincidunt ut laoreet dolore magna aliquam er volutpat.</p>
  </div>
</article>

<footer class="abs footer">
  <div class="fcol" style="left:67px;width:150px">
    <h4>Navigation</h4>
    <ul><li>For Rent</li><li>For Sale</li><li>Property Mangement</li><li>Real Estate</li><li>About</li></ul>
  </div>
  <span class="fsep" style="left:275px"></span>
  <div class="fcol" style="left:343px;width:150px">
    <h4>Other Links</h4>
    <ul><li>Nostrud Exerci</li><li>Blandit Praesent</li><li>Dolore Te Feugait</li><li>Commodo Consequat</li><li>Blandit Praesent</li></ul>
  </div>
  <span class="fsep" style="left:553px"></span>
  <div class="fcol" style="left:623px;width:210px">
    <h4>Get in Touch</h4>
    <div class="contact-line"><svg width="12" height="16" viewBox="0 0 16 20" style="margin-top:4px"><path fill="#999" d="M8 20s8-7.5-8-12.5A8 8 0 010 7.5C0 12.5 8 20 8 20z"/><path fill="#999" d="M8 20S0 12.5 0 7.5a8 8 0 0116 0C16 12.5 8 20 8 20z"/><circle cx="8" cy="7.5" r="3" fill="#2a2a2a"/></svg><span>Harborline Property Group<br>Lorem ipsum dolor sit amet,<br>consectetuer, jantai 123456</span></div>
    <div class="contact-line" style="align-items:center"><svg width="12" height="12" viewBox="0 0 24 24"><path fill="#999" d="M6.6 10.8a15 15 0 006.6 6.6l2.2-2.2c.3-.3.7-.4 1-.2 1.1.4 2.3.6 3.6.6.6 0 1 .4 1 1V20c0 .6-.4 1-1 1A17 17 0 013 4c0-.6.4-1 1-1h3.5c.6 0 1 .4 1 1 0 1.3.2 2.5.6 3.6.1.3 0 .7-.2 1z"/></svg>555 014 2290</div>
    <div class="contact-line" style="align-items:center"><svg width="13" height="10" viewBox="0 0 13 10"><rect width="13" height="10" fill="#999"/><path d="M0 0l6.5 5L13 0" stroke="#2a2a2a" fill="none"/></svg>info@harborlinepg.com</div>
  </div>
  <span class="fsep" style="left:908px"></span>
  <div class="flogo"><div class="name">HARBORLINE</div><div class="sub">PROPERTY GROUP</div></div>
</footer>
<div class="abs copyright">© 2016 Harborline Property Group.</div>

</body>
</html>
```